Flyer design for growing electrical business!!!

looking to get some flyers made for advertising to spread the word about my new business to hopefully create more work!
i am letting potential clients know the type of work i do and am trying to sell my services to them.
To be put on double sided A5. the attached document file has what i would like on each page.
i would like my logo on the first page and and colour scheme of black orange and silver for the flyer following the colours of my logo.
On the second page i would like the photo as a focal point on the top half.
The bold writing are my selling points and would like them accentuated.

```html
<!DOCTYPE html>
<html lang="en">
<head>
<meta charset="utf-8">
<title>Kestrel Volt Electrical – A5 Flyer</title>
<link href="https://fonts.googleapis.com/css2?family=Oswald:wght@500;700&family=Roboto+Condensed:wght@400;700&family=Roboto:wght@400;700&display=swap" rel="stylesheet">
<style>
  :root{
    --orange:#ec5a24;
    --charcoal:#2b2928;
    --white:#ffffff;
    --ink:#222;
    --yellow:#ffe600;
    --row-alt:#e9e9e9;
  }
  *{box-sizing:border-box;margin:0;padding:0}
  html,body{width:1200px;height:1000px;overflow:hidden;background:var(--white)}
  body{position:relative;font-family:"Roboto",Arial,sans-serif}
  .page{position:absolute;top:120px;width:532px;height:745px;overflow:hidden;background:var(--white)}
  .page--front{left:53px}
  .page--back{left:613px}
  .page-bg{position:absolute;inset:0}
  .abs{position:absolute}

  /* front */
  .headline{left:34px;top:22px;font-family:"Oswald",Arial,sans-serif;font-weight:700;font-size:44px;line-height:44px;letter-spacing:.5px}
  .headline .accent{color:var(--orange)}
  .headline .plain{color:#ececec}
  .needs-bar{left:0;top:165px;width:350px;height:28px;background:var(--orange);color:var(--white);font-weight:700;font-size:14.5px;line-height:28px;padding-left:34px;letter-spacing:.3px}
  .needs-bar svg{position:absolute;right:-4px;top:3px}
  .call-today{left:342px;top:21px;width:220px;height:106px;transform:rotate(44deg);transform-origin:center;font-family:"Oswald",Arial,sans-serif;font-weight:700;text-align:center;color:var(--ink);line-height:1}
  .call-today .l1{font-size:26px}
  .call-today .l2{font-size:40px;line-height:38px}
  .call-today .l3{font-size:22px}
  .call-today .free{color:var(--yellow)}
  .call-today .l4{font-size:18px}
  .services{left:34px;top:210px;color:var(--white);font-weight:700;font-size:16.5px;line-height:21px;letter-spacing:.3px}
  .service-list{list-style:none;font-family:"Roboto Condensed",Arial,sans-serif;font-size:18px;color:var(--white);line-height:29.4px}
  .service-list li{position:relative;padding-left:22px}
  .service-list li::before{content:"";position:absolute;left:2px;top:11px;width:12px;height:8px;background:var(--orange);border-radius:4px 1px 1px 4px}
  .service-list li::after{content:"";position:absolute;left:14px;top:12px;width:4px;height:2px;background:var(--orange);box-shadow:0 4px 0 var(--orange)}
  .service-list .wrap{line-height:23px;padding-top:3px;padding-bottom:3px}
  .list-a{left:34px;top:268px}
  .list-b{left:256px;top:268px}
  .brand{left:30px;top:640px;font-weight:700;font-size:17px;line-height:21px;color:var(--orange);display:flex;align-items:center;gap:8px}
  .brand-dot{width:16px;height:16px;border-radius:50%;background:var(--orange);flex:none}
  .contact{left:222px;top:586px;color:var(--ink)}
  .contact .name{font-weight:700;font-size:17px}
  .contact .phone{font-weight:700;color:var(--orange);font-size:26px;line-height:30px}
  .contact .email{font-size:14px;padding-bottom:8px;border-bottom:1px solid #bbb;width:260px}
  .contact .reg{font-size:12px;margin-top:10px}
  .contact .note{font-size:11px;line-height:13px;width:270px;margin-top:2px}

  /* back */
  .photo{left:0;top:0;width:532px;height:320px;background:linear-gradient(180deg,#f4f2ee 0%,#e6e2dc 55%,#b9b3aa 100%)}
  .back-brand{left:420px;top:268px;font-weight:700;font-size:11px;color:var(--orange);display:flex;align-items:center;gap:5px}
  .back-brand .brand-dot{width:10px;height:10px}
  .q{font-weight:700;font-size:14px;line-height:17px;letter-spacing:.2px}
  .q-bill{left:28px;top:333px;color:var(--orange)}
  .q-globes{left:28px;top:383px;color:var(--white)}
  .divider{left:283px;top:330px;width:2px;height:92px;background:#777}
  .divider-arrow{left:284px;top:355px}
  .save{left:309px;top:328px;color:var(--white);font-weight:700}
  .save .up{font-size:19px;line-height:20px}
  .save .amount{color:var(--orange);font-size:31px;line-height:32px}
  .save .bill{font-size:12.5px;line-height:14px}
  .save .basis{color:var(--orange);font-size:11px;line-height:13px}
  .intro{left:28px;top:431px;color:#f0f0f0;font-size:14.6px;line-height:18px}
  .table-title{left:28px;color:var(--white);font-weight:700;font-size:15.5px;line-height:18px;letter-spacing:.1px}
  .tt1{top:481px}
  .tt2{top:587px}
  table{position:absolute;left:28px;width:474px;border-collapse:collapse;font-size:9px;color:var(--ink);text-align:center;table-layout:fixed}
  th{background:var(--orange);color:var(--white);font-weight:700;height:14px;border-right:1px solid var(--charcoal)}
  td{background:var(--white);height:13.5px;border-right:1px solid #bbb;border-top:1px solid #ccc}
  tr:nth-child(even) td{background:var(--row-alt)}
  th:last-child,td:last-child{border-right:0}
  .t1{top:504px}
  .t2{top:610px}
  .change-any{left:28px;top:694px;color:var(--orange);font-weight:700;font-size:11px}
  .types{left:28px;top:708px;color:var(--white);font-size:11px;display:flex;gap:7px}
  .types span::before{content:"";display:inline-block;border-left:4px solid var(--orange);border-top:3.5px solid transparent;border-bottom:3.5px solid transparent;margin-right:4px}
</style>
</head>
<body>

<section class="page page--front" aria-label="Flyer front">
  <svg class="page-bg" width="532" height="745" viewBox="0 0 532 745">
    <defs>
      <linearGradient id="brushed" x1="0" y1="0" x2="1" y2="1">
        <stop offset="0" stop-color="#3a3736"/><stop offset=".5" stop-color="#2c2a29"/><stop offset="1" stop-color="#353231"/>
      </linearGradient>
    </defs>
    <polygon points="0,0 532,0 532,425 380,552 0,552" fill="url(#brushed)"/>
    <polygon points="0,548 377,548 532,420 532,436 384,560 0,560" fill="var(--orange)"/>
    <polygon points="278,0 532,0 532,242" fill="var(--orange)"/>
  </svg>

  <h1 class="abs headline"><span class="accent">LOCAL<br>ELECTRICIAN</span><br><span class="plain">IN YOUR AREA</span></h1>

  <div class="abs needs-bar">FOR ALL YOUR ELECTRICAL NEEDS
    <svg width="26" height="22" viewBox="0 0 26 22"><rect x="2" y="4" width="12" height="14" rx="4" fill="#fff"/><rect x="14" y="6" width="9" height="3" fill="#fff"/><rect x="14" y="13" width="9" height="3" fill="#fff"/><rect x="0" y="10" width="3" height="2" fill="#fff"/></svg>
  </div>

  <div class="abs call-today">
    <div class="l1">CALL</div>
    <div class="l2">TODAY</div>
    <div class="l3">FOR A <span class="free">FREE</span></div>
    <div class="l4">NO OBLIGATION QUOTE</div>
  </div>

  <p class="abs services">NEW INSTALLATIONS - RENOVATIONS<br>ADDITIONS – UPGRADES – REPAIRS – MAINTENANCE</p>

  <ul class="abs service-list list-a">
    <li>Lighting</li><li>LED lighting</li><li>Garden lighting</li><li>Ceiling fans</li><li>Dimmers</li><li>Smoke detectors</li><li>Power points</li><li>Ovens and Cooktops</li><li>Telephone</li>
  </ul>
  <ul class="abs service-list list-b">
    <li>Data</li><li>TV/Aerial</li><li>Switchboard upgrades</li><li class="wrap">Safety switches (RCDS)<br>and Circuit breakers</li><li>Surge protectors</li><li>Hot Water Units</li><li>Test tagging</li>
  </ul>

  <div class="abs brand"><span class="brand-dot"></span><span>KESTREL VOLT<br>ELECTRICAL PTY LTD</span></div>

  <div class="abs contact">
    <div class="name">LIAM CARTER</div>
    <div class="phone">0400 555 182</div>
    <div class="email">hello@kestrelvolt.com</div>
    <div class="reg">ABN 12 345 678 901&nbsp;&nbsp;&nbsp;Lic 100234C</div>
    <div class="note">At Kestrel Volt we are fully insured and all work is completed to current Australian Electrical Standards</div>
  </div>
</section>

<section class="page page--back" aria-label="Flyer back">
  <div class="abs photo" role="img" aria-label="Photo of a bright modern white kitchen with a marble island bench, bar stools, stainless fridge and LED downlights"></div>
  <svg class="page-bg" width="532" height="745" viewBox="0 0 532 745">
    <polygon points="0,310 180,310 532,180 532,745 0,745" fill="var(--charcoal)"/>
    <polygon points="175,310 532,178 532,190 182,318 0,318 0,310" fill="var(--orange)"/>
  </svg>
  <div class="abs back-brand"><span class="brand-dot"></span>KESTREL VOLT</div>

  <p class="abs q q-bill">ARE YOU SPENDING TOO MUCH<br>ON YOUR ELECTRICITY BILL?</p>
  <p class="abs q q-globes">ARE YOU SICK AND TIRED OF<br>CHANGING GLOBES?</p>
  <div class="abs divider"></div>
  <svg class="abs divider-arrow" width="10" height="16" viewBox="0 0 10 16"><polygon points="0,0 9,8 0,16" fill="#888"/></svg>
  <div class="abs save">
    <div class="up">SAVE UP TO</div>
    <div class="amount">$500 OFF</div>
    <div class="bill">YOUR ELECTRICITY BILL</div>
    <div class="basis">BASED ON CHANGING JUST 22 OF<br>YOUR HALOGEN DOWNLIGHTS TO LED</div>
  </div>

  <p class="abs intro">Why not save yourself some money while adding value to your house!<br>LEDs use at least 75% less electricity and last up to 50 times longer</p>

  <h2 class="abs table-title tt1">YEARLY PRICES BASED ON 6 HOURS USE PER DAY @ $0.26 per kWh</h2>
  <table class="t1">
    <tr><th>NUMBER OF DOWNLIGHTS</th><th>HALOGEN GLOBE(50W)</th><th>LED (10W)</th><th>SAVINGS</th></tr>
    <tr><td>1</td><td>$28.47 per year</td><td>$5.69 per year</td><td>$22.78 per year</td></tr>
    <tr><td>10</td><td>$284.70</td><td>$56.90</td><td>$227.80</td></tr>
    <tr><td>20</td><td>$569.40</td><td>$113.80</td><td>$455.60</td></tr>
    <tr><td>30</td><td>$854.10</td><td>$170.70</td><td>$683.40</td></tr>
  </table>

  <h2 class="abs table-title tt2">YEARLY REPLACEMENT COSTS BASED ON 6 HOURS USE PER DAY</h2>
  <table class="t2">
    <tr><th>NUMBER OF DOWNLIGHTS</th><th>HALOGEN (AV. 1000 HOURS)</th><th>LED (AV. 50000 HOURS)</th></tr>
    <tr><td>1</td><td>$8</td><td>$0</td></tr>
    <tr><td>10</td><td>$80</td><td>$0</td></tr>
    <tr><td>20</td><td>$160</td><td>$0</td></tr>
    <tr><td>30</td><td>$240</td><td>$0</td></tr>
  </table>

  <p class="abs change-any">Not just downlights, you can change any light to LED</p>
  <p class="abs types"><span>Oyster lights</span><span>Directional lights</span><span>Spot lights</span><span>Wall lights</span><span>Pendant lights</span><span>External lights</span></p>
</section>

</body>
</html>
```